Window Cleaning Flyer targeting body corporates

Need a flyer for window cleaning targeting body corporate (approx A5 print size). It should be professional and match the logo attached.
We are looking to standout but not be to over the top for a window cleaning/services company.
We want to entice the receptionist or managers to call us because they see no good reason not to.

Industry/Entity Type

Window Cleaning

Font styles to use
Serif

Colors
0555a3
fbed22

Requirements
Must have
• Professional with a few of the photos attached included. Must include logo and the following contact details:
• Ph: 9413 6570
• email: admin@brightpaneworks.com.au
• PO Box 4726
• Marlowe Heights
• 3284
Nice to have
• Colours matching logo/ van print layout. Looking for more of a simplistic professional design.
Should not have
• Cartoon pictures, animated decorations or stock photos.

```html
<!DOCTYPE html>
<html lang="en">
<head>
<meta charset="utf-8">
<title>Brightpane Window Cleaning – Body Corporate Flyer</title>
<link href="https://fonts.googleapis.com/css2?family=Arimo:wght@400;700&family=Oswald:wght@600&family=Catamaran:wght@600;700&family=Open+Sans:wght@600&display=swap" rel="stylesheet">
<style>
  :root {
    --backdrop: #e8e6e2;
    --header-blue: #2b7cc6;
    --body-blue: #0a55a0;
    --band-blue: #2a78c2;
    --brand-yellow: #fbed22;
    --white: #ffffff;
    --ink: #111111;
  }
  * { margin: 0; padding: 0; box-sizing: border-box; }
  html, body { width: 1200px; height: 1000px; overflow: hidden; }
  body { background: var(--backdrop); position: relative; font-family: "Arimo", Arial, sans-serif; }

  .flyer {
    position: absolute; left: 250px; top: 8px; width: 694px; height: 967px;
    background: var(--white); overflow: hidden;
    box-shadow: 0 4px 14px rgba(0,0,0,0.25);
  }

  .header { position: absolute; left: 0; top: 0; width: 694px; height: 137px; background: var(--header-blue); }
  .brand { position: absolute; left: 47px; top: 40px; color: var(--brand-yellow); font-weight: 700; line-height: 1; }
  .brand__name { font-size: 40px; letter-spacing: 1px; display: block; }
  .brand__tagline { font-size: 17px; display: block; margin-top: 10px; letter-spacing: 0.3px; }

  .contact { position: absolute; left: 455px; top: 39px; list-style: none; color: var(--white);
    font-family: "Open Sans", Arial, sans-serif; font-weight: 600; font-size: 12.5px; line-height: 18.6px; }
  .contact li { position: relative; padding-left: 25px; }
  .contact svg { position: absolute; left: 0; top: 4px; width: 11px; height: 11px; }

  .hero-photo {
    position: absolute; left: 0; top: 144px; width: 694px; height: 356px;
    background: linear-gradient(160deg, #3d4a58 0%, #7f95ab 35%, #a9c6e0 60%, #5d7687 80%, #1f2a3a 100%);
  }
  .call-badge {
    position: absolute; left: 429px; top: 160px; width: 237px; height: 220px; border-radius: 50%;
    background: var(--brand-yellow); border: 5px solid var(--white);
    box-shadow: 4px 5px 6px rgba(0,0,0,0.3);
    font-family: "Catamaran", Arial, sans-serif; font-weight: 700; color: var(--ink);
  }
  .call-badge__label { position: absolute; left: 26px; top: 46px; font-size: 35px; line-height: 1; }
  .call-badge__number { position: absolute; left: 26px; top: 98px; font-size: 41px; line-height: 1; letter-spacing: 0.5px; }

  .services { position: absolute; left: 0; top: 512px; width: 694px; height: 455px; background: var(--body-blue); }
  .services__heading { position: absolute; left: 0; top: 20px; width: 694px; text-align: center;
    font-family: "Oswald", Arial, sans-serif; font-weight: 600; font-size: 28px; color: var(--white); }

  .service { position: absolute; color: var(--brand-yellow); }
  .service__title { font-weight: 700; font-size: 24px; line-height: 1; position: relative; }
  .service__title svg { position: absolute; left: -28px; top: 7px; width: 12px; height: 10px; }
  .service__detail { color: var(--white); font-weight: 700; font-size: 14.5px; line-height: 22px; margin-top: 6px; }
  .service--windows { left: 71px; top: 100px; }
  .service--gutters { left: 387px; top: 100px; }
  .service--gutters .service__detail { padding-left: 5px; }
  .service--pressure { left: 231px; top: 213px; }

  .experience-band { position: absolute; left: 0; top: 330px; width: 694px; height: 125px; }
  .experience-band__text { position: absolute; left: 38px; top: 44px; color: var(--white);
    font-weight: 700; font-size: 15.5px; line-height: 28px; }

  .quote-box {
    position: absolute; left: 485px; top: 772px; width: 209px; height: 176px;
    background: var(--brand-yellow); border: 4px solid var(--white); border-right: none;
    box-shadow: 2px 3px 5px rgba(0,0,0,0.3);
    font-family: "Catamaran", Arial, sans-serif; font-weight: 700; color: var(--ink);
    text-align: center; line-height: 1.15; padding-top: 4px;
  }
  .quote-box span { display: block; }
  .quote-box__small { font-size: 19px; }
  .quote-box__big { font-size: 23px; }
  .quote-box__small-inline { font-size: 18px; }
</style>
</head>
<body>
  <main class="flyer">
    <header class="header">
      <div class="brand">
        <span class="brand__name">BRIGHTPANE</span>
        <span class="brand__tagline">WINDOW CLEANING</span>
      </div>
      <ul class="contact">
        <li><svg viewBox="0 0 12 12"><path fill="#fff" d="M1 4c0-2 2-3 5-3s5 1 5 3l-3 1-1-1H5L4 5zM3 6h6l2 5H1z"/></svg>9413 6570</li>
        <li><svg viewBox="0 0 12 12"><rect x="1" y="2.5" width="10" height="7" fill="#fff"/><path d="M1 3l5 4 5-4" stroke="#2b7cc6" stroke-width="1.2" fill="none"/></svg>admin@brightpaneworks.com.au</li>
        <li><svg viewBox="0 0 12 12"><circle cx="6" cy="6" r="5" fill="#fff"/><circle cx="6" cy="6" r="2" fill="#2b7cc6"/></svg>PO Box 4726</li>
        <li>Marlowe Heights</li>
        <li>3284</li>
      </ul>
    </header>

    <div class="hero-photo" role="img" aria-label="Photo of two window cleaners using long-handled squeegees on a glass shopfront under a blue sky"></div>

    <div class="call-badge">
      <span class="call-badge__label">call us:</span>
      <span class="call-badge__number">9413 6570</span>
    </div>

    <section class="services">
      <h1 class="services__heading">BRIGHTPANE&nbsp; specialises&nbsp; in Body Corporate</h1>

      <div class="service service--windows">
        <div class="service__title"><svg viewBox="0 0 12 10"><path d="M1 5l3.5 3.5L11 1.5" stroke="#fff" stroke-width="2" fill="none"/></svg>Window Cleaning</div>
      </div>
      <div class="service service--gutters">
        <div class="service__title"><svg viewBox="0 0 12 10"><path d="M1 5l3.5 3.5L11 1.5" stroke="#fff" stroke-width="2" fill="none"/></svg>Gutter Cleaning</div>
        <p class="service__detail">Using Our Ladder Free<br>Gutter Vaccum</p>
      </div>
      <div class="service service--pressure">
        <div class="service__title"><svg viewBox="0 0 12 10"><path d="M1 5l3.5 3.5L11 1.5" stroke="#fff" stroke-width="2" fill="none"/></svg>Pressure Washing</div>
        <p class="service__detail">Including Moss Treatment to<br>Prevent Mould regrowth<br>on Concrete Surface</p>
      </div>

      <div class="experience-band">
        <svg width="694" height="125" viewBox="0 0 694 125" style="position:absolute;left:0;top:0">
          <polygon points="0,8 694,8 694,125 0,125" fill="#2a78c2"/>
          <polygon points="0,0 480,0 470,8 0,8" fill="#0a55a0"/>
          <polygon points="470,8 520,40 694,40 694,8" fill="#1f6bb4"/>
        </svg>
        <p class="experience-band__text">With over 15 years of experience we will ensure<br>the job is completed to the highest standard everytime</p>
      </div>
    </section>

    <aside class="quote-box">
      <span class="quote-box__small">contact</span>
      <span class="quote-box__big">BRIGHTPANE TEAM</span>
      <span class="quote-box__big"><span class="quote-box__small-inline" style="display:inline">for an </span>EASY ,</span>
      <span class="quote-box__big">FREE</span>
      <span class="quote-box__big">QUOTE <span class="quote-box__small-inline" style="display:inline">TODAY</span></span>
    </aside>
  </main>
</body>
</html>
```